KPV Construction we build lodges in Botswana

We need a Design Layout only with Categories where we can update each projects photos.... We have a web address and a host - kpv.construction

```html
<!DOCTYPE html>
<html lang="en">
<head>
<meta charset="utf-8">
<title>KPV Construction – Website Layout</title>
<link rel="stylesheet" href="https://fonts.googleapis.com/css2?family=Orbitron:wght@500;700;900&family=Jost:wght@400;500;600&display=swap">
<style>
:root{
  --red:#e3151f;
  --red-dark:#b80f17;
  --blue:#1467bd;
  --blue-dark:#0d4f96;
  --ink:#333;
  --muted:#777;
  --canvas:#efefef;
  --white:#fff;
  --dark:#221c18;
  --dark-2:#3a2f27;
  --map:#e6e9e1;
  --map-soft:#d3e2c6;
  --head:"Orbitron",sans-serif;
  --body:"Jost",sans-serif;
}
*{box-sizing:border-box;margin:0;padding:0}
html,body{width:1200px;height:2381px;overflow:hidden;background:var(--canvas)}
body{font-family:var(--body);color:var(--ink)}
.canvas{position:relative;width:1200px;height:2381px;overflow:hidden;background:var(--canvas)}
.bands{position:absolute;inset:0;width:1200px;height:2381px}

/* showcase heading */
.showcase-brand{position:absolute;top:52px;left:0;width:1200px;text-align:center}
.showcase-brand .brand-square{display:block;width:74px;height:74px;margin:0 auto 22px;background:var(--red)}
.showcase-brand .brand-name{font-family:var(--head);font-weight:700;font-size:22px;letter-spacing:1px;color:var(--blue)}

.brief{position:absolute;top:300px;text-align:center}
.brief--home{left:70px;width:501px}
.brief--project{left:630px;width:500px}
.brief-title{font-family:var(--head);font-weight:700;font-size:16px;letter-spacing:2px}
.brief-desc{margin:12px auto 0;width:340px;font-size:11.5px;line-height:16px;color:#444}
.t-red{color:var(--red)}
.t-blue{color:var(--blue)}

.thank-you{position:absolute;top:2264px;left:0;width:1200px;text-align:center;font-family:var(--head);font-weight:900;font-size:25px;letter-spacing:3px}

/* mockups */
.mock{position:absolute;top:384px;background:var(--white);overflow:hidden;box-shadow:0 4px 18px rgba(0,0,0,.18)}
.mock--home{left:70px;width:501px;height:1775px}
.mock--project{left:630px;width:500px;height:1060px}
.block{position:absolute;left:0;width:100%}

/* site header */
.site-header{top:0;height:30px;background:var(--white)}
.brand-mini{position:absolute;left:30px;top:6px;display:flex;align-items:center;gap:4px}
.brand-mini .sq{width:11px;height:11px;background:var(--red)}
.brand-mini .nm{font-family:var(--head);font-weight:700;font-size:5.5px;color:var(--blue);letter-spacing:.3px}
.contact-bits{position:absolute;right:10px;top:6px;display:flex;align-items:center;gap:14px}
.contact-bit{display:flex;align-items:center;gap:4px}
.ico-box{width:12px;height:12px;border-radius:2px;background:var(--red);display:flex;align-items:center;justify-content:center}
.ico-box svg{width:7px;height:7px}
.contact-bit small{display:block;font-size:4px;color:var(--muted)}
.contact-bit b{display:block;font-size:4.8px;font-weight:500;color:var(--ink)}
.social-dots{display:flex;gap:2px}
.social-dots i{width:8px;height:8px;border-radius:50%;background:var(--red)}
.site-nav{position:absolute;top:30px;left:144px;right:0;height:12px;background:var(--blue);display:flex;align-items:stretch;padding-left:8px}
.site-nav a{display:flex;align-items:center;padding:0 9px;font-family:var(--head);font-size:4.4px;color:var(--white);letter-spacing:.3px}
.site-nav a.is-active{background:var(--red)}

/* hero */
.hero{top:42px;height:232px}
.hero-photo{position:absolute;inset:0;background:linear-gradient(180deg,#a7c0d6 0%,#8aa1b5 25%,#7a5737 48%,#5e3f26 68%,#8e8a84 100%)}
.hero-photo--project{background:linear-gradient(180deg,#2f4b70 0%,#5b7594 35%,#6b4c33 62%,#4a3624 85%,#7c766d 100%)}
.hero-shade{position:absolute;inset:0;background:rgba(0,0,0,.22)}
.hero-copy{position:absolute;left:0;right:0;top:78px;text-align:center;color:var(--white)}
.hero-copy h1{font-family:var(--head);font-weight:700;font-size:13px;line-height:17px;letter-spacing:1.5px}
.hero-copy p{margin-top:3px;font-size:4.6px;letter-spacing:.3px}
.btn{display:inline-flex;align-items:center;gap:4px;height:11px;padding:0 9px;border-radius:6px;font-family:var(--head);font-size:4.5px;color:var(--white);letter-spacing:.3px}
.btn--red{background:var(--red)}
.btn--blue{background:var(--blue)}
.btn .dot{width:8px;height:8px;border-radius:50%;background:var(--white);margin-left:-7px;display:flex;align-items:center;justify-content:center}
.btn .dot svg{width:5px;height:5px}
.hero-copy .btn{margin-top:9px}
.hero-notch{position:absolute;left:0;bottom:-1px;width:100%;height:34px}

/* section heading */
.sec-head{position:absolute;left:0;width:100%;text-align:center}
.sec-title{font-family:var(--head);font-weight:700;font-size:10px;letter-spacing:1.5px}
.sec-title--light{color:var(--white)}
.sec-mark{display:block;width:5px;height:5px;margin:5px auto 0;border:1px solid var(--red);transform:rotate(45deg)}
.sec-mark--light{border-color:var(--white)}

/* who we are */
.about-media{position:absolute;left:87px;top:346px;width:153px;height:106px;background:linear-gradient(160deg,#6f8fa6 0%,#9a7350 40%,#c39b6c 70%,#7d6a55 100%);box-shadow:0 2px 6px rgba(0,0,0,.2)}
.play-btn{position:absolute;left:66px;top:44px;width:20px;height:14px;border-radius:3px;background:var(--red);display:flex;align-items:center;justify-content:center}
.play-btn svg{width:7px;height:7px}
.about-copy{position:absolute;left:255px;top:350px;width:215px}
.about-copy h4{font-family:var(--head);font-weight:700;font-size:6.2px;color:var(--blue);letter-spacing:.3px}
.about-copy h5{margin-top:3px;font-size:4.6px;font-weight:600;color:var(--ink)}
.about-copy p{margin-top:4px;font-size:4.3px;line-height:6.4px;color:var(--muted)}
.about-copy .btn{margin-top:9px;margin-left:8px}

/* what we do */
.services{top:470px;height:276px}
.services-bg{position:absolute;inset:0;width:100%;height:100%}
.service-cards{position:absolute;top:74px;left:89px;display:flex;gap:13px}
.service-card{width:98px;height:178px;background:var(--blue);box-shadow:0 3px 8px rgba(0,0,0,.25)}
.service-photo{height:100px;border:3px solid var(--white);border-bottom:0}
.service-photo--a{background:linear-gradient(170deg,#233553 0%,#6a4a2f 50%,#d39a52 75%,#4d3a2a 100%)}
.service-photo--b{background:linear-gradient(170deg,#9bb2c9 0%,#7a5f48 45%,#5c5149 70%,#8d7b69 100%)}
.service-photo--c{background:linear-gradient(170deg,#8fb6dc 0%,#b8c9d8 40%,#b08457 65%,#6f5a44 100%)}
.service-body{padding:8px 7px;color:var(--white)}
.service-body h6{font-family:var(--head);font-weight:500;font-size:4.6px;line-height:6.5px;letter-spacing:.3px}
.service-body p{margin-top:4px;font-size:4px;line-height:6px;opacity:.9}
.slide-arrow{position:absolute;width:12px;height:12px;border-radius:50%;background:var(--white);display:flex;align-items:center;justify-content:center}
.slide-arrow svg{width:5px;height:5px}

/* our projects (home) */
.tabs{position:absolute;left:0;width:100%;display:flex;justify-content:center;align-items:center;gap:10px}
.tab{font-size:4.3px;color:var(--ink);padding:2px 6px}
.tab.is-active{background:var(--blue);color:var(--white);border-radius:6px;font-family:var(--head);font-size:4px}
.showcase-row{position:absolute;top:814px;left:86px;height:119px}
.showcase-side{position:absolute;top:4px;width:77px;height:111px;background:linear-gradient(160deg,#cfcfcf 0%,#8f8f8f 45%,#5c5c5c 100%)}
.showcase-main{position:absolute;top:0;left:78px;width:165px;height:119px;border:3px solid var(--blue);background:linear-gradient(170deg,#3f5a3c 0%,#7a6a4c 35%,#c79c63 60%,#a07649 85%,#8b7a66 100%)}
.showcase-caption{position:absolute;top:944px;left:0;width:100%;text-align:center}
.showcase-caption h6{font-family:var(--head);font-weight:700;font-size:5.5px;color:var(--ink);letter-spacing:.3px}
.showcase-caption p{margin:4px auto 0;width:170px;font-size:4.2px;line-height:6px;color:var(--muted)}
.showcase-caption .btn{margin-top:8px}

/* why choose us */
.why{top:1020px;height:210px}
.why-bg{position:absolute;inset:0;width:100%;height:100%}
.why-mark{position:absolute;left:222px;top:86px;width:58px;height:58px;background:var(--white);display:flex;align-items:center;justify-content:center;text-align:center;font-family:var(--head);font-weight:700;font-size:6px;line-height:9px;color:var(--blue);box-shadow:0 2px 6px rgba(0,0,0,.25)}
.feature{position:absolute;display:flex;align-items:center;gap:4px;color:var(--white);font-family:var(--head);font-size:4.2px;line-height:6px;letter-spacing:.2px}
.feature--left{flex-direction:row-reverse;text-align:right}
.feature .ico-box{width:14px;height:14px;flex:none}
.feature .ico-box svg{width:8px;height:8px}

/* testimonials */
.bubble{position:absolute;padding:6px 8px;font-size:4.3px;line-height:6.2px;color:var(--white)}
.bubble--red{left:105px;top:1303px;width:143px;height:43px;background:var(--red)}
.bubble--blue{left:248px;top:1316px;width:134px;height:42px;background:var(--blue)}
.bubble::after{content:"";position:absolute;left:14px;bottom:-6px;border-right:6px solid transparent}
.bubble--red::after{border-top:6px solid var(--red)}
.bubble--blue::after{border-top:6px solid var(--blue)}
.client{position:absolute;display:flex;align-items:center;gap:6px}
.avatar{width:20px;height:20px;background:linear-gradient(180deg,#d9d9d9,#a9a9a9);border:2px solid var(--white);box-shadow:0 1px 3px rgba(0,0,0,.25)}
.client b{display:block;font-size:4.6px;font-weight:600;color:var(--blue)}
.client .stars{font-size:5px;color:#f2b01e;letter-spacing:.5px}
.round-arrow{position:absolute;width:11px;height:11px;border-radius:50%;border:1px solid #ccc;display:flex;align-items:center;justify-content:center}
.round-arrow svg{width:4px;height:4px}

/* map placeholder */
.map{background:linear-gradient(120deg,var(--map) 0%,var(--map-soft) 100%)}

/* footer */
.footer{height:223px}
.footer-bg{position:absolute;inset:0;width:100%;height:100%}
.subscribe{position:absolute;top:32px;left:0;width:100%;text-align:center}
.subscribe h5{font-family:var(--body);font-weight:500;font-size:8px;color:var(--white);letter-spacing:.3px}
.subscribe-form{display:flex;justify-content:center;margin-top:8px}
.subscribe-form span{width:145px;height:12px;background:var(--white);font-size:4.2px;color:#999;display:flex;align-items:center;padding-left:5px}
.subscribe-form b{width:52px;height:12px;background:var(--blue);font-size:4.3px;font-weight:500;color:var(--white);display:flex;align-items:center;justify-content:center;letter-spacing:.3px}
.footer-cols{position:absolute;top:92px;left:89px;right:20px;height:100px}
.fcol{position:absolute;top:0;color:#ddd;font-size:4.2px;line-height:9.5px}
.fcol h6{font-family:var(--head);font-weight:500;font-size:5px;color:var(--white);letter-spacing:.5px;margin-bottom:7px}
.fcol li{list-style:none;padding-left:6px;position:relative}
.fcol li::before{content:"";position:absolute;left:0;top:4px;width:2px;height:2px;background:var(--red)}
.fcol .info{display:flex;gap:3px;line-height:5.5px;margin-bottom:5px}
.fcol .info i{flex:none;width:4px;height:4px;margin-top:1px;border-radius:50%;background:var(--blue)}
.fcol .field{width:76px;height:9px;background:var(--white);margin-bottom:3px;font-size:3.8px;color:#999;padding-left:3px;line-height:9px}
.fcol .field--tall{height:17px}
.fcol .btn{height:9px;padding:0 6px;border-radius:5px;font-size:3.8px}
.follow-name{font-family:var(--head);font-weight:700;font-size:5px;color:var(--white);line-height:7px;margin-top:6px}
.follow-dots{display:flex;gap:5px;margin-top:6px}
.follow-dots i{width:6px;height:6px;border-radius:50%;background:rgba(255,255,255,.75)}
.copyright{position:absolute;left:15px;right:15px;bottom:6px;display:flex;justify-content:space-between;font-size:3.6px;color:#aaa;border-top:1px solid rgba(255,255,255,.12);padding-top:4px}

/* project page */
.tile-grid{position:absolute;top:322px;left:88px;display:grid;grid-template-columns:repeat(3,100px);grid-auto-rows:72px;gap:14px 12px}
.tile{position:relative;box-shadow:0 1px 3px rgba(0,0,0,.2)}
.tile--a{background:linear-gradient(160deg,#8fb0cc 0%,#a58058 55%,#6f5238 100%)}
.tile--b{background:linear-gradient(160deg,#c9c3b7 0%,#b5875a 50%,#7b5c3f 100%)}
.tile--c{background:linear-gradient(160deg,#6d8a5e 0%,#8a7a63 50%,#5c4b3a 100%)}
.tile--d{background:linear-gradient(160deg,#9cb9d4 0%,#c59a66 55%,#9a7148 100%)}
.tile--e{background:linear-gradient(160deg,#5d7552 0%,#a3835f 55%,#d2b284 100%)}
.tile--hover{background:var(--red);color:var(--white);text-align:center;padding:9px 8px}
.tile--hover h6{font-family:var(--head);font-weight:500;font-size:4.3px;letter-spacing:.3px}
.tile--hover p{margin-top:4px;font-size:3.8px;line-height:5.4px}
.tile--hover i{display:block;width:9px;height:9px;margin:5px auto 0;border-radius:50%;background:var(--white);color:var(--red);font-style:normal;font-size:7px;line-height:9px;font-weight:600}
.pager{position:absolute;top:668px;left:0;width:100%;display:flex;justify-content:center;gap:7px;font-size:4.6px;color:var(--blue);align-items:center}
.pager .word{font-family:var(--head);font-size:4px;margin:0 10px}
.pager b{color:var(--red);font-weight:600}
</style>
</head>
<body>
<div class="canvas">

  <svg class="bands" viewBox="0 0 1200 2381" aria-hidden="true">
    <polygon points="1200,341 1200,476 0,1111 0,762" fill="#e3151f"/>
    <polygon points="0,1508 1200,1968 1200,2302 0,1746" fill="#1467bd"/>
  </svg>

  <header class="showcase-brand">
    <span class="brand-square"></span>
    <span class="brand-name">KPV CONSTRUCTION</span>
  </header>

  <section class="brief brief--home">
    <h2 class="brief-title"><span class="t-red">HOMEPAGE</span> <span class="t-blue">DESIGN</span></h2>
    <p class="brief-desc">Custom Homepage Design to show About company and other important works at a glance and for contact.</p>
  </section>

  <section class="brief brief--project">
    <h2 class="brief-title"><span class="t-red">PROJECT PAGE</span> <span class="t-blue">DESIGN</span></h2>
    <p class="brief-desc">This is Our Project page were you can upload Picture of All your projects to show your Customer.</p>
  </section>

  <!-- HOMEPAGE -->
  <article class="mock mock--home">
    <div class="block site-header">
      <div class="brand-mini"><span class="sq"></span><span class="nm">KPV CONSTRUCTION</span></div>
      <div class="contact-bits">
        <div class="contact-bit">
          <span class="ico-box"><svg viewBox="0 0 10 10"><path d="M2 1l2 2-1 1.2c.6 1.2 1.6 2.2 2.8 2.8L7 6l2 2-1.3 1.3C4.6 9 1 5.4.7 2.3z" fill="#fff"/></svg></span>
          <span><small>Call Us</small><b>+267 555 0142</b></span>
        </div>
        <div class="contact-bit">
          <span class="ico-box"><svg viewBox="0 0 10 10"><rect x="1" y="2.5" width="8" height="5.5" fill="#fff"/><path d="M1 2.5l4 3 4-3" stroke="#e3151f" stroke-width=".8" fill="none"/></svg></span>
          <span><small>Email</small><b>info@kpv.construction</b></span>
        </div>
        <div class="social-dots"><i></i><i></i><i></i></div>
      </div>
    </div>
    <nav class="site-nav"><a class="is-active">HOME</a><a>ABOUT US</a><a>SERVICE</a><a>PROJECT</a><a>SOLUTIONS</a><a>CONTACT US</a></nav>

    <section class="block hero">
      <div class="hero-photo" role="img" aria-label="Photo of a large timber log lodge with a stone driveway"></div>
      <div class="hero-shade"></div>
      <div class="hero-copy">
        <h1>WE ARE A<br>CONSTRUCTION COMPANY</h1>
        <p>BUILDERS OF TIMBER LODGES AND LOG HOMES ACROSS BOTSWANA</p>
        <span class="btn btn--red">GET STARTED</span>
      </div>
      <svg class="hero-notch" viewBox="0 0 501 34" preserveAspectRatio="none" aria-hidden="true">
        <polygon points="0,2 250,32 0,34" fill="#fff"/>
        <polygon points="501,2 250,32 501,34" fill="#fff"/>
        <polyline points="0,2 250,32 501,2" fill="none" stroke="#1467bd" stroke-width="1.5"/>
      </svg>
    </section>

    <div class="sec-head" style="top:308px"><h3 class="sec-title"><span class="t-blue">WHO WE</span> <span class="t-red">ARE</span></h3><span class="sec-mark"></span></div>
    <div class="about-media" role="img" aria-label="Video still of a log home under construction in a forest">
      <span class="play-btn"><svg viewBox="0 0 10 10"><path d="M3 2l5 3-5 3z" fill="#fff"/></svg></span>
    </div>
    <div class="about-copy">
      <h4>WE ARE A CONSTRUCTION COMPANY</h4>
      <h5>BASED IN BOTSWANA, BUILDING TIMBER LODGES AND LOG HOMES</h5>
      <p>We design and raise hand-built timber homes, safari lodges and resorts. Every project is planned with care, from the first drawing to the final roof beam, using strong local and imported wood.</p>
      <p>Our crews work closely with each client so the finished building fits the land, the budget and the way people want to live.</p>
      <span class="btn btn--blue"><span class="dot"><svg viewBox="0 0 10 10"><path d="M3 2l4 3-4 3" stroke="#1467bd" stroke-width="1.6" fill="none"/></svg></span>LEARN MORE</span>
    </div>

    <section class="block services">
      <svg class="services-bg" viewBox="0 0 501 276" preserveAspectRatio="none" aria-hidden="true">
        <polygon points="0,26 250,0 501,26 501,252 250,276 0,252" fill="#e3151f"/>
      </svg>
      <div class="sec-head" style="top:20px"><h3 class="sec-title sec-title--light">WHAT WE DO</h3><span class="sec-mark sec-mark--light"></span></div>
      <span class="slide-arrow" style="left:54px;top:158px"><svg viewBox="0 0 10 10"><path d="M7 2L3 5l4 3" stroke="#e3151f" stroke-width="1.8" fill="none"/></svg></span>
      <span class="slide-arrow" style="left:435px;top:158px"><svg viewBox="0 0 10 10"><path d="M3 2l4 3-4 3" stroke="#e3151f" stroke-width="1.8" fill="none"/></svg></span>
      <div class="service-cards">
        <div class="service-card"><div class="service-photo service-photo--a" role="img" aria-label="Photo of a lit log home at dusk"></div><div class="service-body"><h6>LOG<br>HOMES</h6><p>Solid log houses built by hand for family living and quiet retreats.</p></div></div>
        <div class="service-card"><div class="service-photo service-photo--b" role="img" aria-label="Photo of a post and beam cabin"></div><div class="service-body"><h6>LOG POST AND<br>BEAM</h6><p>Open timber frames with wide spans and bright, tall rooms.</p></div></div>
        <div class="service-card"><div class="service-photo service-photo--c" role="img" aria-label="Photo of a lodge roof frame"></div><div class="service-body"><h6>LODGE AND RESORT<br>CONSTRUCTION</h6><p>Guest lodges and resort cabins for safari and travel hosts.</p></div></div>
      </div>
    </section>

    <div class="sec-head" style="top:752px"><h3 class="sec-title"><span class="t-red">OUR</span> <span class="t-blue">PROJECTS</span></h3><span class="sec-mark"></span></div>
    <div class="tabs" style="top:785px"><span class="tab">Exterior Designs</span><span class="tab is-active">CONSTRUCTION WORK</span><span class="tab">Kitchen, Baths &amp; Bedrooms</span><span class="tab">Decks And Other Projects</span></div>
    <div class="showcase-row">
      <div class="showcase-side" style="left:0" role="img" aria-label="Greyscale photo of a timber frame project"></div>
      <div class="showcase-main" role="img" aria-label="Photo of a log lodge under construction"></div>
      <div class="showcase-side" style="left:250px" role="img" aria-label="Greyscale photo of a finished cabin interior"></div>
    </div>
    <div class="showcase-caption">
      <h6>CONSTRUCTION WORK</h6>
      <p>Framing, walls and roofs raised by our own crews on every site we build.</p>
      <span class="btn btn--red"><span class="dot"><svg viewBox="0 0 10 10"><path d="M3 2l4 3-4 3" stroke="#e3151f" stroke-width="1.6" fill="none"/></svg></span>VIEW ALL PROJECT</span>
    </div>

    <section class="block why">
      <svg class="why-bg" viewBox="0 0 501 210" preserveAspectRatio="none" aria-hidden="true">
        <polygon points="0,0 501,0 501,188 250,208 0,188" fill="#1467bd"/>
        <polyline points="0,188 250,208 501,188" fill="none" stroke="#e3151f" stroke-width="2"/>
      </svg>
      <div class="sec-head" style="top:16px"><h3 class="sec-title sec-title--light">WHY CHOOSE US</h3><span class="sec-mark sec-mark--light"></span></div>
      <div class="why-mark">KPV<br>CONSTRUCTION</div>

      <div class="feature feature--left" style="right:284px;top:60px"><span class="ico-box"><svg viewBox="0 0 10 10"><path d="M2 8l4-4M5 2l3 3-1.5 1.5-3-3z" stroke="#fff" stroke-width="1.2" fill="none"/></svg></span><span>HAND BUILT<br>DESIGN</span></div>
      <div class="feature feature--left" style="right:329px;top:114px"><span class="ico-box"><svg viewBox="0 0 10 10"><path d="M1.5 5L5 2l3.5 3v3.5h-7z" fill="#fff"/></svg></span><span>TOTAL HOME<br>SOLUTION</span></div>
      <div class="feature feature--left" style="right:284px;top:163px"><span class="ico-box"><svg viewBox="0 0 10 10"><circle cx="5" cy="5" r="2.6" stroke="#fff" stroke-width="1.4" fill="none"/><circle cx="5" cy="5" r=".8" fill="#fff"/></svg></span><span>CAD &amp; DRAFTING<br>SERVICES</span></div>

      <div class="feature" style="left:282px;top:60px"><span class="ico-box"><svg viewBox="0 0 10 10"><rect x="2" y="2" width="6" height="6" fill="#fff"/></svg></span><span>RETROFIT CONSTRUCTION<br>SOLUTIONS</span></div>
      <div class="feature" style="left:326px;top:114px"><span class="ico-box"><svg viewBox="0 0 10 10"><path d="M2 8V3h2v5M6 8V2h2v6" fill="#fff"/></svg></span><span>RE-BUILDING<br>BUILDING</span></div>
      <div class="feature" style="left:282px;top:163px"><span class="ico-box"><svg viewBox="0 0 10 10"><path d="M2 5l2 2 4-4" stroke="#fff" stroke-width="1.5" fill="none"/></svg></span><span>LOG CONSTRUCTION<br>SERVICE</span></div>
    </section>

    <div class="sec-head" style="top:1262px"><h3 class="sec-title"><span class="t-blue">CLIENT</span> <span class="t-blue">TESTIMONIALS</span></h3><span class="sec-mark"></span></div>
    <span class="round-arrow" style="left:73px;top:1330px"><svg viewBox="0 0 10 10"><path d="M7 2L3 5l4 3" stroke="#999" stroke-width="1.6" fill="none"/></svg></span>
    <span class="round-arrow" style="left:417px;top:1330px"><svg viewBox="0 0 10 10"><path d="M3 2l4 3-4 3" stroke="#999" stroke-width="1.6" fill="none"/></svg></span>
    <div class="bubble bubble--red">The crew built our lodge on time and the timber work is beautiful. We would gladly hire them again for our next camp.</div>
    <div class="bubble bubble--blue">Clear plans, fair pricing and a solid log home that stays cool in summer. Great team from start to finish.</div>
    <div class="client" style="left:113px;top:1368px"><span class="avatar" role="img" aria-label="Client portrait"></span><span><b>DANA MOKOENA</b><span class="stars">★★★★★</span></span></div>
    <div class="client" style="left:256px;top:1376px"><span class="avatar" role="img" aria-label="Client portrait"></span><span><b>LESEDI KGOSI</b><span class="stars">★★★★★</span></span></div>

    <div class="block map" style="top:1420px;height:140px" role="img" aria-label="Map showing the company location"></div>

    <footer class="block footer" style="top:1552px">
      <svg class="footer-bg" viewBox="0 0 501 223" preserveAspectRatio="none" role="img" aria-label="Dark photo of a timber frame site">
        <defs><linearGradient id="fh" x1="0" y1="0" x2="0" y2="1"><stop offset="0" stop-color="#3a2f27"/><stop offset="1" stop-color="#1c1714"/></linearGradient></defs>
        <polygon points="0,24 250,0 501,24 501,223 0,223" fill="url(#fh)"/>
        <polyline points="0,24 250,0 501,24" fill="none" stroke="#1467bd" stroke-width="2"/>
      </svg>
      <div class="subscribe">
        <h5>SUBSCRIBE TO RECEIVE UPDATES!</h5>
        <div class="subscribe-form"><span>Enter Email Address</span><b>SUBSCRIBE</b></div>
      </div>
      <div class="footer-cols">
        <div class="fcol" style="left:0"><h6>QUICK LINKS</h6><ul><li>Home</li><li>About Us</li><li>Service</li><li>Project</li><li>Contact Us</li></ul></div>
        <div class="fcol" style="left:76px;width:80px"><h6>CONTACT INFO</h6>
          <div class="info"><i></i><span>KPV CONSTRUCTION<br>Plot 14, Main Road<br>Maun, Botswana</span></div>
          <div class="info"><i></i><span>+267 555 0142</span></div>
          <div class="info"><i></i><span>info@kpv.construction</span></div>
        </div>
        <div class="fcol" style="left:173px"><h6>QUICK CONTACT</h6><div class="field">Name</div><div class="field">Email</div><div class="field field--tall">Message</div><span class="btn btn--red">SUBMIT NOW</span></div>
        <div class="fcol" style="left:274px"><h6>FOLLOW US</h6><div class="follow-name">KPV<br>CONSTRUCTION</div><div class="follow-dots"><i></i><i></i><i></i></div></div>
      </div>
      <div class="copyright"><span>© Copyright KPV Construction. All rights reserved.</span><span>Privacy Policy</span></div>
    </footer>
  </article>

  <!-- PROJECT PAGE -->
  <article class="mock mock--project">
    <div class="block site-header">
      <div class="brand-mini"><span class="sq"></span><span class="nm">KPV CONSTRUCTION</span></div>
      <div class="contact-bits">
        <div class="contact-bit">
          <span class="ico-box"><svg viewBox="0 0 10 10"><path d="M2 1l2 2-1 1.2c.6 1.2 1.6 2.2 2.8 2.8L7 6l2 2-1.3 1.3C4.6 9 1 5.4.7 2.3z" fill="#fff"/></svg></span>
          <span><small>Call Us</small><b>+267 555 0142</b></span>
        </div>
        <div class="contact-bit">
          <span class="ico-box"><svg viewBox="0 0 10 10"><rect x="1" y="2.5" width="8" height="5.5" fill="#fff"/><path d="M1 2.5l4 3 4-3" stroke="#e3151f" stroke-width=".8" fill="none"/></svg></span>
          <span><small>Email</small><b>info@kpv.construction</b></span>
        </div>
        <div class="social-dots"><i></i><i></i><i></i></div>
      </div>
    </div>
    <nav class="site-nav"><a>HOME</a><a>ABOUT US</a><a>SERVICE</a><a class="is-active">PROJECT</a><a>SOLUTIONS</a><a>CONTACT US</a></nav>

    <section class="block hero" style="height:186px">
      <div class="hero-photo hero-photo--project" role="img" aria-label="Evening photo of a timber lodge with mountains behind"></div>
      <div class="hero-shade"></div>
      <div class="hero-copy" style="top:74px"><h1>OUR PROJECTS</h1></div>
      <svg class="hero-notch" viewBox="0 0 500 34" preserveAspectRatio="none" aria-hidden="true">
        <polygon points="0,2 250,32 0,34" fill="#fff"/>
        <polygon points="500,2 250,32 500,34" fill="#fff"/>
        <polyline points="0,2 250,32 500,2" fill="none" stroke="#1467bd" stroke-width="1.5"/>
      </svg>
    </section>

    <div class="sec-head" style="top:251px"><h3 class="sec-title"><span class="t-blue">BROWSE OUR</span> <span class="t-red">PROJECTS</span></h3><span class="sec-mark"></span></div>
    <div class="tabs" style="top:294px"><span class="tab">Exterior Designs</span><span class="tab is-active">CONSTRUCTION WORK</span><span class="tab">Kitchen, Baths &amp; Bedrooms</span><span class="tab">Decks And Other Projects</span></div>

    <div class="tile-grid">
      <div class="tile tile--a" role="img" aria-label="Project photo: roof trusses"></div>
      <div class="tile tile--hover"><h6>CONSTRUCTION WORK</h6><p>Log walls raised on site by our framing crew.</p><i>+</i></div>
      <div class="tile tile--d" role="img" aria-label="Project photo: open timber ceiling"></div>
      <div class="tile tile--c" role="img" aria-label="Project photo: cleared building plot"></div>
      <div class="tile tile--b" role="img" aria-label="Project photo: foundation slab"></div>
      <div class="tile tile--e" role="img" aria-label="Project photo: stacked log walls"></div>
      <div class="tile tile--e" role="img" aria-label="Project photo: log wall corner"></div>
      <div class="tile tile--b" role="img" aria-label="Project photo: lodge exterior"></div>
      <div class="tile tile--a" role="img" aria-label="Project photo: finished log cabin"></div>
      <div class="tile tile--d" role="img" aria-label="Project photo: timber frame with crane"></div>
      <div class="tile tile--c" role="img" aria-label="Project photo: post and beam frame"></div>
      <div class="tile tile--b" role="img" aria-label="Project photo: roof framing"></div>
    </div>
    <div class="pager"><span class="word">PREVIOUS</span><span>1</span><b>2</b><span>3</span><span>4...10</span><span class="word">NEXT</span></div>

    <div class="block map" style="top:708px;height:140px" role="img" aria-label="Map showing the company location"></div>

    <footer class="block footer" style="top:838px">
      <svg class="footer-bg" viewBox="0 0 500 223" preserveAspectRatio="none" role="img" aria-label="Dark photo of a timber frame site">
        <defs><linearGradient id="fp" x1="0" y1="0" x2="0" y2="1"><stop offset="0" stop-color="#3a2f27"/><stop offset="1" stop-color="#1c1714"/></linearGradient></defs>
        <polygon points="0,24 250,0 500,24 500,223 0,223" fill="url(#fp)"/>
        <polyline points="0,24 250,0 500,24" fill="none" stroke="#1467bd" stroke-width="2"/>
      </svg>
      <div class="subscribe">
        <h5>SUBSCRIBE TO RECEIVE UPDATES!</h5>
        <div class="subscribe-form"><span>Enter Email Address</span><b>SUBSCRIBE</b></div>
      </div>
      <div class="footer-cols">
        <div class="fcol" style="left:0"><h6>QUICK LINKS</h6><ul><li>Home</li><li>About Us</li><li>Service</li><li>Project</li><li>Contact Us</li></ul></div>
        <div class="fcol" style="left:76px;width:80px"><h6>CONTACT INFO</h6>
          <div class="info"><i></i><span>KPV CONSTRUCTION<br>Plot 14, Main Road<br>Maun, Botswana</span></div>
          <div class="info"><i></i><span>+267 555 0142</span></div>
          <div class="info"><i></i><span>info@kpv.construction</span></div>
        </div>
        <div class="fcol" style="left:173px"><h6>QUICK CONTACT</h6><div class="field">Name</div><div class="field">Email</div><div class="field field--tall">Message</div><span class="btn btn--red">SUBMIT NOW</span></div>
        <div class="fcol" style="left:274px"><h6>FOLLOW US</h6><div class="follow-name">KPV<br>CONSTRUCTION</div><div class="follow-dots"><i></i><i></i><i></i></div></div>
      </div>
      <div class="copyright"><span>© Copyright KPV Construction. All rights reserved.</span><span>Privacy Policy</span></div>
    </footer>
  </article>

  <p class="thank-you"><span class="t-red">THANK</span> <span class="t-blue">YOU</span></p>
</div>
</body>
</html>
```